BOLD & MINIMALIST DESIGN NEEDED

We want a very bold but minimalistic business card design that is impactful and utilizes both sides of the business card. Our current logo is included for your use.

We want bold fonts and good use of negative space. We don't want the logo to overpower the design.

Target Market(s)

Professionals who are building new commercial buildings.

Industry/Entity Type

Construction

Contact Information for Business Card

Name, Title, email, office phone, cell phone, website

Font styles to use
Serif
Sans Serif

Requirements
Must have
• Bold design!

```html
<!DOCTYPE html>
<html lang="en">
<head>
<meta charset="utf-8">
<title>Ridgeline Design + Build — Business Card</title>
<link href="https://fonts.googleapis.com/css2?family=Montserrat:wght@400;500;600;700;800&display=swap" rel="stylesheet">
<style>
  :root {
    --backdrop: #d9dadc;
    --card: #ffffff;
    --ink: #000000;
    --paper-text: #ffffff;
  }
  * { margin: 0; padding: 0; box-sizing: border-box; }
  html, body {
    width: 1200px;
    height: 900px;
    overflow: hidden;
    background: var(--backdrop);
    font-family: "Montserrat", sans-serif;
    color: var(--ink);
  }
  .stage { position: relative; width: 1200px; height: 900px; }

  .card {
    position: absolute;
    width: 513px;
    height: 293px;
    background: var(--card);
    overflow: hidden;
  }

  /* Front */
  .card--front { left: 218px; top: 123px; }
  .front-band {
    position: absolute;
    left: 353px; top: 0;
    width: 160px; height: 100%;
    background: var(--ink);
  }
  .brand-mark {
    position: absolute;
    left: 252px; top: 140px;
    width: 36px; height: 36px;
    background: var(--ink);
  }
  .brand-name {
    position: absolute;
    left: 304px; top: 10px;
    height: 274px;
    writing-mode: vertical-rl;
    transform: rotate(180deg);
    text-align: center;
    font-weight: 800;
    font-size: 44px;
    line-height: 46px;
    letter-spacing: 0.5px;
    color: var(--ink);
  }
  .brand-tagline {
    position: absolute;
    left: 358px; top: 36px;
    height: 220px;
    writing-mode: vertical-rl;
    transform: rotate(180deg);
    text-align: center;
    font-weight: 400;
    font-size: 15px;
    line-height: 20px;
    letter-spacing: 4.5px;
    color: var(--paper-text);
  }

  /* Back */
  .card--back { left: 470px; top: 476px; width: 513px; height: 292px; }
  .back-band {
    position: absolute;
    left: 0; top: 0;
    width: 82px; height: 100%;
    background: var(--ink);
  }
  .contact-keys {
    position: absolute;
    left: 54px; top: 165px;
    list-style: none;
    color: var(--paper-text);
    font-size: 11px;
    font-weight: 500;
    line-height: 17.5px;
    text-align: center;
    width: 12px;
  }
  .holder-name {
    position: absolute;
    left: 101px; top: 40px;
    font-weight: 700;
    font-size: 28px;
    letter-spacing: 1.5px;
    line-height: 32px;
  }
  .holder-title {
    position: absolute;
    left: 101px; top: 76px;
    font-weight: 700;
    font-size: 13px;
    letter-spacing: 1.2px;
  }
  .contact-list {
    position: absolute;
    left: 101px; top: 163px;
    list-style: none;
    font-weight: 500;
    font-size: 12.5px;
    letter-spacing: 1.1px;
    line-height: 17.5px;
  }
  .contact-web {
    position: absolute;
    left: 101px; top: 236px;
    font-weight: 500;
    font-size: 12.5px;
    letter-spacing: 1.1px;
  }
  .back-brand {
    position: absolute;
    right: 40px; top: 210px;
    font-weight: 800;
    font-size: 15px;
    letter-spacing: 0.5px;
  }
</style>
</head>
<body>
<main class="stage">

  <section class="card card--front" aria-label="Card front">
    <div class="front-band"></div>
    <span class="brand-mark" aria-hidden="true"></span>
    <h1 class="brand-name">RIDGELINE</h1>
    <p class="brand-tagline">DESIGN + BUILD</p>
  </section>

  <section class="card card--back" aria-label="Card back">
    <div class="back-band"></div>
    <ul class="contact-keys" aria-hidden="true">
      <li>P</li>
      <li>M</li>
      <li>E</li>
    </ul>
    <h2 class="holder-name">DANA REYES</h2>
    <p class="holder-title">PROJECT MANAGER</p>
    <ul class="contact-list">
      <li>+1 (555) 014-2290</li>
      <li>+6012 5550 1234</li>
      <li>DANA@RIDGELINE.COM</li>
    </ul>
    <p class="contact-web">WWW.RIDGELINE.COM</p>
    <p class="back-brand">RIDGELINE</p>
  </section>

</main>
</body>
</html>
```